Maple Ridge business card design

Card needs to include the following text/items:
Company Logo
Tobin Marsh
Phone # - 555-318-7642
service@mapleridgelandscaping.example
Lawn & landscape maintenance services

```html
<!DOCTYPE html>
<html lang="en">
<head>
<meta charset="utf-8">
<title>Maple Ridge Landscaping – Business Card</title>
<link rel="stylesheet" href="https://fonts.googleapis.com/css2?family=Cinzel:wght@700&family=Montserrat:wght@400;600;700&family=Roboto+Condensed:wght@400&display=swap">
<style>
  :root {
    --backdrop: #d9d9d9;
    --card: #f1f1f1;
    --card-back: #e4e4e4;
    --forest: #1c4424;
    --forest-deep: #12301a;
    --leaf: #6f9434;
    --sky: #4aa9dc;
    --ink: #222;
    --ink-soft: #3a3a3a;
    --white: #ffffff;
  }
  * { margin: 0; padding: 0; box-sizing: border-box; }
  html, body { width: 1200px; height: 831px; overflow: hidden; }
  body { background: var(--backdrop); position: relative; font-family: "Montserrat", sans-serif; }

  .card {
    position: absolute;
    left: 308px;
    width: 576px;
    height: 332px;
    overflow: hidden;
    box-shadow: 0 2px 6px rgba(0,0,0,.18);
  }
  .card--front { top: 57px; background: var(--card); }
  .card--back { top: 429px; background: var(--card-back); }

  .brand-mark {
    position: absolute;
    border-radius: 50%;
    border: 3px solid var(--leaf);
    background: linear-gradient(180deg, var(--sky) 0%, var(--sky) 28%, var(--forest) 55%, var(--forest-deep) 100%);
  }
  .card--front .brand-mark { left: 198px; top: 48px; width: 180px; height: 180px; }
  .card--back .brand-mark { left: 296px; top: 84px; width: 278px; height: 278px; }

  .wordmark {
    position: absolute;
    font-family: "Cinzel", serif;
    font-weight: 700;
    color: var(--forest);
    text-align: center;
    line-height: 1;
    white-space: nowrap;
  }
  .wordmark__name { display: block; letter-spacing: -0.5px; }
  .wordmark__trade { display: block; }

  .card--front .wordmark { left: 0; right: 0; top: 230px; }
  .card--front .wordmark__name { font-size: 42px; }
  .card--front .wordmark__trade { font-size: 18px; letter-spacing: 0.78em; margin-right: -0.78em; margin-top: 6px; }

  .card--back .wordmark { left: 27px; top: 16px; text-align: left; }
  .card--back .wordmark__name { font-size: 48px; }
  .card--back .wordmark__trade { font-size: 20px; letter-spacing: 0.82em; margin-top: 6px; }

  .contact { position: absolute; left: 19px; top: 168px; }
  .contact__name {
    font-family: "Cinzel", serif;
    font-weight: 700;
    font-size: 27px;
    color: var(--forest);
    line-height: 1;
    white-space: nowrap;
  }
  .contact__role { font-size: 15px; color: var(--ink-soft); margin-top: 6px; }
  .contact__list { list-style: none; margin-top: 14px; }
  .contact__item {
    display: flex;
    align-items: center;
    gap: 9px;
    font-family: "Roboto Condensed", sans-serif;
    font-size: 15px;
    color: var(--ink);
    height: 24px;
    white-space: nowrap;
  }
  .contact__item svg { width: 15px; height: 15px; flex: none; fill: var(--forest); }

  .tagline-band {
    position: absolute;
    left: 0; right: 0; bottom: 0;
    height: 23px;
    background: var(--forest);
    color: var(--white);
    font-weight: 700;
    font-size: 15px;
    text-align: center;
    line-height: 23px;
  }
</style>
</head>
<body>

<section class="card card--front">
  <div class="brand-mark" role="img" aria-label="Round landscape emblem area: sky, hills and trees"></div>
  <h1 class="wordmark">
    <span class="wordmark__name">Maple Ridge</span>
    <span class="wordmark__trade">LANDSCAPING</span>
  </h1>
</section>

<section class="card card--back">
  <div class="wordmark">
    <span class="wordmark__name">Maple Ridge</span>
    <span class="wordmark__trade">LANDSCAPING</span>
  </div>

  <div class="brand-mark" role="img" aria-label="Round landscape emblem area: sky, hills and trees"></div>

  <div class="contact">
    <p class="contact__name">Tobin Marsh</p>
    <p class="contact__role">Managing Director</p>
    <ul class="contact__list">
      <li class="contact__item">
        <svg viewBox="0 0 24 24" aria-hidden="true"><path d="M6.6 10.8a15.1 15.1 0 0 0 6.6 6.6l2.2-2.2a1 1 0 0 1 1-.25 11.4 11.4 0 0 0 3.6.57 1 1 0 0 1 1 1V20a1 1 0 0 1-1 1A17 17 0 0 1 3 4a1 1 0 0 1 1-1h3.5a1 1 0 0 1 1 1c0 1.25.2 2.45.57 3.57a1 1 0 0 1-.25 1z"/></svg>
        <span>555-318-7642</span>
      </li>
      <li class="contact__item">
        <svg viewBox="0 0 24 24" aria-hidden="true"><path d="M2 5h20v14H2z M3.5 6.5 12 13l8.5-6.5" fill="var(--forest)" stroke="var(--card-back)" stroke-width="1.4"/></svg>
        <span>service@mapleridgelandscaping.example</span>
      </li>
    </ul>
  </div>

  <p class="tagline-band">Lawn &amp; landscape maintenance services</p>
</section>

</body>
</html>
```